Marlow Ridge Dental business card

Business card would have following info:

Alden R. Kasprzak, DMD, FAGD
General Dentist
email: office@marlowridgedental.example
phone: 617-490-3867
fax: 617-490-3867
website: marlowridgedental.example

second side would have lines for:

appointment date
appointment time

```html
<!DOCTYPE html>
<html lang="en">
<head>
<meta charset="utf-8">
<title>Marlow Ridge Dental – Business Card</title>
<link rel="stylesheet" href="https://fonts.googleapis.com/css2?family=Montserrat:wght@600;700;800&family=Open+Sans:wght@400;600&display=swap">
<style>
  :root {
    --backdrop: #c4c4c4;
    --brand-blue: #0a4f7e;
    --rule-blue: #1f5a8a;
    --accent-orange: #f2901e;
    --card-white: #ffffff;
    --ink-dark: #2b2b2b;
    --ink-grey: #4a4a4a;
  }
  * { box-sizing: border-box; margin: 0; padding: 0; }
  html, body { width: 1200px; height: 815px; overflow: hidden; }
  body {
    background: var(--backdrop);
    display: flex;
    align-items: center;
    justify-content: center;
    gap: 40px;
    font-family: "Open Sans", sans-serif;
  }
  .card {
    width: 540px;
    height: 310px;
    border-radius: 26px;
    border-bottom: 5px solid var(--accent-orange);
    position: relative;
    overflow: hidden;
    box-shadow: 0 10px 24px rgba(0,0,0,0.18);
  }

  /* Front */
  .card-front {
    background: var(--card-white);
    display: flex;
    align-items: center;
    justify-content: center;
    gap: 22px;
    padding: 0 30px;
  }
  .identity { text-align: right; }
  .identity-name {
    font-family: "Montserrat", sans-serif;
    font-weight: 800;
    font-size: 19px;
    color: var(--brand-blue);
    letter-spacing: 0.5px;
    text-transform: uppercase;
  }
  .identity-credentials {
    font-family: "Montserrat", sans-serif;
    font-weight: 800;
    font-size: 17px;
    color: var(--accent-orange);
    margin-top: 2px;
  }
  .identity-role {
    font-size: 12px;
    color: var(--ink-grey);
    letter-spacing: 1px;
    text-transform: uppercase;
    margin-top: 3px;
  }
  .divider {
    width: 2px;
    height: 92px;
    background: var(--rule-blue);
  }
  .contact-list { list-style: none; }
  .contact-item {
    display: flex;
    align-items: center;
    gap: 8px;
    font-size: 12.5px;
    color: var(--ink-dark);
    line-height: 22px;
  }
  .contact-icon { width: 12px; height: 12px; flex: none; fill: var(--accent-orange); }

  /* Back */
  .card-back {
    background: var(--brand-blue);
    color: var(--card-white);
    padding: 34px 34px 0 38px;
  }
  .practice-name {
    font-family: "Montserrat", sans-serif;
    font-weight: 800;
    font-size: 50px;
    line-height: 50px;
    text-transform: uppercase;
    letter-spacing: 1px;
    margin-left: 54px;
  }
  .appointment-heading {
    font-family: "Montserrat", sans-serif;
    font-weight: 700;
    font-size: 15px;
    color: var(--accent-orange);
    text-transform: uppercase;
    margin: 16px 0 0 100px;
    display: inline-block;
    padding-bottom: 5px;
    border-bottom: 1.5px solid var(--accent-orange);
  }
  .appointment-fields {
    display: flex;
    align-items: baseline;
    gap: 8px;
    margin-top: 20px;
    font-size: 13px;
  }
  .field-line {
    flex: 1;
    border-bottom: 1.5px dashed var(--card-white);
    transform: translateY(-3px);
  }
  .weekday-row {
    display: flex;
    justify-content: space-between;
    margin-top: 22px;
    font-size: 13px;
  }
  .weekday { display: flex; align-items: center; gap: 6px; }
  .weekday-box {
    width: 11px; height: 11px;
    border: 2px solid var(--accent-orange);
  }
</style>
</head>
<body>

  <section class="card card-front" aria-label="Business card front">
    <div class="identity">
      <p class="identity-name">Alden R. Kasprzak</p>
      <p class="identity-credentials">DMD, FAGD</p>
      <p class="identity-role">General Dentist</p>
    </div>
    <div class="divider"></div>
    <ul class="contact-list">
      <li class="contact-item">
        <svg class="contact-icon" viewBox="0 0 12 12" aria-hidden="true"><path d="M2.5 0.8 L4.4 3 L3.4 4.3 Q4.6 6.9 7.7 8.6 L9 7.6 L11.2 9.5 L9.9 11.2 Q4.5 10.4 0.8 2.1 Z"/></svg>
        617-490-3867
      </li>
      <li class="contact-item">
        <svg class="contact-icon" viewBox="0 0 12 12" aria-hidden="true"><rect x="3" y="0.5" width="6" height="3.5"/><rect x="0.5" y="4.5" width="11" height="5" rx="1"/><rect x="3" y="8" width="6" height="3.5"/></svg>
        617-490-3867
      </li>
      <li class="contact-item">
        <svg class="contact-icon" viewBox="0 0 12 12" aria-hidden="true"><path d="M0.5 2.5 H11.5 V9.5 H0.5 Z M1.2 3 L6 6.8 L10.8 3" stroke="#fff" stroke-width="0.8"/></svg>
        office@marlowridgedental.example
      </li>
      <li class="contact-item">
        <svg class="contact-icon" viewBox="0 0 12 12" aria-hidden="true"><circle cx="6" cy="6" r="5.5"/><path d="M0.8 6 H11.2 M6 0.6 Q3 6 6 11.4 M6 0.6 Q9 6 6 11.4" stroke="#fff" stroke-width="0.8" fill="none"/></svg>
        www.marlowridgedental.example
      </li>
    </ul>
  </section>

  <section class="card card-back" aria-label="Business card back">
    <h1 class="practice-name">Marlow<br>Ridge Dental</h1>
    <h2 class="appointment-heading">Your Appointment</h2>
    <div class="appointment-fields">
      <span>Date</span><span class="field-line"></span>
      <span>Time</span><span class="field-line"></span>
      <span>am/pm</span>
    </div>
    <div class="weekday-row">
      <span class="weekday"><span class="weekday-box"></span>Mon</span>
      <span class="weekday"><span class="weekday-box"></span>Tues</span>
      <span class="weekday"><span class="weekday-box"></span>Wed</span>
      <span class="weekday"><span class="weekday-box"></span>Thur</span>
      <span class="weekday"><span class="weekday-box"></span>Fri</span>
      <span class="weekday"><span class="weekday-box"></span>Sat</span>
    </div>
  </section>

</body>
</html>
```